Business card design needed

Hello, I Need a business card for a company that specialises in providing contract management services for civil construction projects - roads, bridges etc.
I do have a logo that i produced for PLOVER Civilworks however it probably needs a little work, the circles dont have defined edges, i was thinking the colours should reflect the dry interior of Australia progressing out to the colours of the ocean as you move towards the East.... that was my thinking anyway!
Target Market(s)
Professional people generally 30+ yrs old who need professional services to deliver contracts in a high risk environment
Industry/Entity Type
Construction
Contact Information for Business Card
PLOVER Civilworks
Darren Pollock - Director and Principal Engineer
Registered Professional Engineer of Queensland
Phone 0491 265 807
Email darren@plovercivilworks.com.au
ABN 48 213 670 194
Logo Text
PLOVER Civilworks
Logo styles of interest
Pictorial/Combination Logo
Wordmark Logo
Lettermark Logo
Look and feel

```html
<!DOCTYPE html>
<html lang="en">
<head>
<meta charset="utf-8">
<title>PLOVER Civilworks – Business Card</title>
<link rel="stylesheet" href="https://fonts.googleapis.com/css2?family=Montserrat:wght@400;500&display=swap">
<style>
  :root {
    --backdrop: #e9eaec;
    --card-white: #f7f8f8;
    --card-navy: #2b3442;
    --ink-navy: #2a3240;
    --teal: #3e6a72;
    --teal-light: #c9e4da;
    --grey-text: #4a5058;
  }
  * { box-sizing: border-box; margin: 0; padding: 0; }
  html, body {
    width: 1200px; height: 901px; overflow: hidden;
    background: var(--backdrop);
    font-family: "Montserrat", Arial, sans-serif;
  }
  .canvas {
    position: relative; width: 1200px; height: 901px;
  }
  .card {
    position: absolute; left: 280px;
    width: 640px; height: 388px;
    box-shadow: 0 6px 18px rgba(0,0,0,0.18);
    overflow: hidden;
  }
  .card--front { top: 40px; background: var(--card-white); }
  .card--back { top: 472px; background: var(--card-navy); }

  .brand {
    position: absolute; display: flex; align-items: center; gap: 14px;
    font-weight: 500; letter-spacing: 0.5px; white-space: nowrap;
  }
  .brand__dot { border-radius: 50%; flex: none; }
  .card--front .brand { left: 52px; top: 64px; font-size: 36px; color: var(--ink-navy); }
  .card--front .brand__dot { width: 40px; height: 40px; background: var(--teal); }
  .card--back .brand { left: 110px; top: 168px; font-size: 38px; color: #ffffff; }
  .card--back .brand__dot { width: 42px; height: 42px; background: var(--teal-light); }

  .contact {
    position: absolute; left: 150px; top: 150px;
    padding-left: 18px; height: 178px;
    border-left: 2px solid var(--teal);
    color: var(--grey-text);
  }
  .contact__name { font-size: 30px; color: var(--teal); font-weight: 400; line-height: 1.1; }
  .contact__role { font-size: 13.5px; line-height: 1.3; margin-top: 4px; }
  .contact__lines { margin-top: 22px; font-size: 19px; line-height: 1.3; color: var(--ink-navy); }
  .contact__label { color: var(--teal); margin-right: 6px; }
  .contact__abn { margin-top: 18px; font-size: 14px; }

  .band {
    position: absolute; left: 0; right: 0; bottom: 0; height: 46px;
    background: var(--teal);
  }
</style>
</head>
<body>
<div class="canvas">
  <section class="card card--front">
    <div class="brand">
      <span class="brand__dot"></span>
      <span class="brand__name">PLOVER Civilworks</span>
    </div>
    <div class="contact">
      <p class="contact__name">Darren Pollock</p>
      <p class="contact__role">Director and Principal Engineer<br>Registered Professional Engineer of Queensland</p>
      <p class="contact__lines">
        <span class="contact__label">Phone</span>0491 265 807<br>
        <span class="contact__label">Email</span>darren@plovercivilworks.com.au
      </p>
      <p class="contact__abn">ABN 48 213 670 194</p>
    </div>
    <div class="band"></div>
  </section>

  <section class="card card--back">
    <div class="brand">
      <span class="brand__dot"></span>
      <span class="brand__name">PLOVER Civilworks</span>
    </div>
  </section>
</div>
</body>
</html>
```